Unique and original Business Card for Financial Services Business

I have moved premises and need to change the detail on my business card so thought now is a good time for a re-design. Looking for something professional and modern with colours to fit in with out logo. Like the idea of foil or embossing if that works but not a must have but I do want something that stands out and that I could not design myself.

Once business card is designed I will also be looking to get letterhead and flyers done but want the business card concept in place first.

The majority of designs I am receiving are generic and template based. I am looking for something unique and original. We have some great design elements in our logo, think outside the box and show me something that stands out from the crowd.

Target Market(s)

Business Professionals

Industry/Entity Type

Finance

Contact Information for Business Card

Name: Delia Norwood Phone 0473 958 162 Address PO Box 8617 Mossvale NSW 2389 Email info@steadyharbourfinancialservices.com.au website www.steadyharbourfinancialservices.com.au

Font styles to use
Other font styles liked:
• Ralway

Requirements
Should not have
• No black backgrounds please

```html
<!DOCTYPE html>
<html lang="en">
<head>
<meta charset="utf-8">
<title>Steady Harbour Financial Services – Business Card</title>
<link href="https://fonts.googleapis.com/css2?family=Montserrat:wght@400;500;600;700&display=swap" rel="stylesheet">
<style>
  :root {
    --page-bg: #ffffff;
    --card-white: #ffffff;
    --stripe: #f1f3f4;
    --teal-light: #00a59d;
    --teal-mid: #027a80;
    --navy-deep: #0b3550;
    --brand-text: #0f7f86;
    --ornament: #c9cdcf;
    --text-light: #ffffff;
    --shadow: rgba(0, 0, 0, 0.28);
  }
  * { box-sizing: border-box; margin: 0; padding: 0; }
  html, body {
    width: 849px;
    height: 1200px;
    overflow: hidden;
    background: var(--page-bg);
    font-family: "Montserrat", Arial, sans-serif;
  }
  .canvas {
    position: relative;
    width: 849px;
    height: 1200px;
  }
  .card {
    position: absolute;
    width: 347px;
    height: 229px;
    box-shadow: 8px 9px 10px var(--shadow);
    overflow: hidden;
  }
  .card--front { left: 57px; top: 98px; background: var(--card-white); }
  .card--back {
    left: 432px; top: 97px; height: 230px;
    background: linear-gradient(90deg, var(--navy-deep) 0%, var(--teal-mid) 50%, var(--teal-light) 100%);
  }
  .card__art { position: absolute; inset: 0; width: 100%; height: 100%; }

  .brand {
    position: absolute;
    display: flex;
    align-items: center;
    gap: 7px;
    color: var(--brand-text);
    font-weight: 500;
    text-transform: uppercase;
    line-height: 1.05;
  }
  .brand__mark {
    width: 12px; height: 12px;
    background: currentColor;
    flex: none;
  }
  .brand__name { font-size: 15px; letter-spacing: 0.2px; }
  .brand__tag { display: block; font-size: 8.5px; letter-spacing: 2.6px; margin-top: 3px; }

  .card--front .brand { left: 22px; top: 40px; }

  .card--back .brand {
    left: 0; right: 0; top: 92px;
    justify-content: center;
    color: var(--text-light);
  }

  .hummingbird {
    position: absolute;
    left: 28px; top: 126px;
    width: 56px; height: 66px;
    border-radius: 40% 55% 45% 50%;
    background: linear-gradient(160deg, var(--teal-mid), var(--navy-deep));
    opacity: 0.9;
  }

  .contact {
    position: absolute;
    right: 19px;
    top: 100px;
    text-align: right;
    color: var(--text-light);
  }
  .contact__name { font-size: 13px; font-weight: 700; letter-spacing: 0.3px; text-transform: uppercase; }
  .contact__phone { font-size: 10.5px; font-weight: 600; margin-top: 20px; }
  .contact__address { font-size: 8.8px; font-weight: 500; margin-top: 7px; line-height: 1.35; }
  .contact__email { font-size: 7.6px; font-weight: 500; margin-top: 5px; }
  .contact__web { font-size: 9px; font-weight: 700; margin-top: 4px; }
</style>
</head>
<body>
<main class="canvas">

  <section class="card card--front" aria-label="Business card front">
    <svg class="card__art" viewBox="0 0 347 229" preserveAspectRatio="none" aria-hidden="true">
      <defs>
        <linearGradient id="front-panel" x1="0" y1="1" x2="1" y2="0">
          <stop offset="0" stop-color="#0b3550"/>
          <stop offset="0.5" stop-color="#02717b"/>
          <stop offset="1" stop-color="#00a59d"/>
        </linearGradient>
      </defs>
      <polygon points="0,0 60,0 0,70" fill="#f1f3f4"/>
      <polygon points="90,0 150,0 0,175 0,105" fill="#f1f3f4"/>
      <polygon points="180,0 230,0 30,229 0,229 0,210" fill="#f4f6f7"/>
      <polygon points="275,0 347,0 347,229 68,229" fill="url(#front-panel)"/>
    </svg>
    <svg class="card__art" viewBox="0 0 347 229" preserveAspectRatio="none" role="img" aria-label="Decorative ornament border along the diagonal edge">
      <polygon points="270,0 282,0 75,229 63,229" fill="#c9cdcf" opacity="0.7"/>
    </svg>

    <div class="brand">
      <span class="brand__mark"></span>
      <span><span class="brand__name">Steady Harbour</span><span class="brand__tag">Financial Services</span></span>
    </div>

    <div class="hummingbird" role="img" aria-label="Teal hummingbird illustration"></div>

    <div class="contact">
      <p class="contact__name">Delia Norwood</p>
      <p class="contact__phone">0473 958 162</p>
      <p class="contact__address">PO Box 8617<br>Mossvale NSW 2389</p>
      <p class="contact__email">info@steadyharbourfinancialservices.com.au</p>
      <p class="contact__web">www.steadyharbourfinancialservices.com.au</p>
    </div>
  </section>

  <section class="card card--back" aria-label="Business card back">
    <div class="brand">
      <span class="brand__mark"></span>
      <span><span class="brand__name">Steady Harbour</span><span class="brand__tag">Financial Services</span></span>
    </div>
  </section>

</main>
</body>
</html>
```